Personal Finance e-commerce website needs a simple budget design

Hello! I am starting to sell downloadable and printable budget planners, as shown in the attached file, for people to plan ahead on their personal finances. <br/><br/>I want to see a one-page design with similar columns (for example, "Expenses, Budget, and Actual"). I would also like to see the basic formula ("Net Income = Gross income - Total Expenses") somewhere on the design. Finally, I want the design to remain mostly minimalistic and simple for the average person to plan their personal monthly budgets.<br/><br/>However, other than that, the overall design, layout, and colors will be at the graphic designer's choice. If you have any questions for me, please let me know. Thank you for your time!

Industry/Entity Type

Financial Planning

Colors

Designer to choose colors to be used in the design.

Requirements
Must have
• I want to see a one-page design with similar columns (for example, "Expenses, Budget, and Actual").
• I want the design to remain mostly minimalistic and simple for the average person to plan their personal monthly budgets.
Nice to have
• I would also like to see the basic formula ("Net Income = Gross income - Total Expenses") somewhere on the design.

```html
<!DOCTYPE html>
<html lang="en">
<head>
<meta charset="utf-8">
<title>Basic Monthly Budget</title>
<link href="https://fonts.googleapis.com/css2?family=Poppins:wght@300;400;500;600;700;800&display=swap" rel="stylesheet">
<style>
  :root {
    --backdrop: #4aa6cb;
    --paper: #eeeef0;
    --ink: #111111;
    --cat-head: #5d5f64;
    --cat-body: #cfd0d5;
    --plan-head: #6aa57a;
    --plan-body: #a9cab2;
    --actual-head: #6c9fc4;
    --actual-body: #cbdae6;
    --formula: #e1d700;
    --formula-note: #e2e2e5;
    --rule: #3a3a3a;
  }
  * { box-sizing: border-box; margin: 0; padding: 0; }
  html, body {
    width: 1180px; height: 1200px; overflow: hidden;
    background: var(--backdrop);
    font-family: "Poppins", sans-serif;
    color: var(--ink);
  }
  .sheet {
    position: absolute; left: 160px; top: 36px;
    width: 860px; height: 1128px;
    background: var(--paper);
    padding: 0 60px;
  }
  .brand {
    position: absolute; right: 52px; top: 62px;
    font-weight: 400; font-size: 30px; letter-spacing: 7px;
  }
  .title {
    position: absolute; left: 56px; top: 100px;
    font-weight: 700; font-size: 70px; letter-spacing: -1.5px; line-height: 1;
  }
  .period {
    position: absolute; left: 60px; top: 190px;
    font-size: 23px; display: flex; align-items: baseline;
  }
  .period .fill {
    display: inline-block; border-bottom: 2px dotted var(--rule);
    margin: 0 6px 0 6px; height: 1px;
  }
  .fill.month { width: 152px; }
  .fill.year { width: 182px; }
  .ledger {
    position: absolute; left: 60px; top: 254px; width: 741px;
    display: grid; grid-template-columns: repeat(3, 241px); column-gap: 9px;
  }
  .column-head {
    height: 55px; display: flex; align-items: center; justify-content: center;
    color: #f4f4f4; font-weight: 600; font-size: 23px;
  }
  .column-body { height: 620px; }
  .column-body .hint {
    height: 84px; padding-top: 20px; text-align: center; font-size: 17px;
  }
  .column-body .line {
    height: 53.6px; border-top: 1.5px dashed var(--rule);
  }
  .category .column-head { background: var(--cat-head); }
  .category .column-body { background: var(--cat-body); }
  .plan .column-head { background: var(--plan-head); }
  .plan .column-body { background: var(--plan-body); }
  .actual .column-head { background: var(--actual-head); }
  .actual .column-body { background: var(--actual-body); }
  .formula {
    position: absolute; left: 60px; top: 938px; width: 741px;
  }
  .formula-bar {
    height: 48px; background: var(--formula);
    display: grid; grid-template-columns: 1fr 30px 1fr 30px 1fr;
    align-items: center; text-align: center;
    font-weight: 600; font-size: 25px;
  }
  .formula-bar .term { position: relative; }
  .formula-bar .term::after {
    content: ""; position: absolute; left: 50%; bottom: -16px;
    transform: translateX(-50%);
    border: 7px solid transparent; border-top-color: var(--formula);
  }
  .formula-notes {
    height: 50px; background: var(--formula-note);
    display: grid; grid-template-columns: 1fr 30px 1fr 30px 1fr;
    align-items: center; text-align: center;
    font-size: 14px; line-height: 1.3; text-transform: uppercase;
  }
  .footer {
    position: absolute; left: 60px; top: 1066px; width: 741px;
    text-align: center; font-size: 24px;
  }
  .footer strong { font-weight: 700; }
</style>
</head>
<body>
  <main class="sheet">
    <div class="brand">HARLOW FINCH</div>
    <h1 class="title">Basic Monthly Budget</h1>
    <div class="period">
      Month<span class="fill month"></span>Year<span class="fill year"></span>
    </div>

    <section class="ledger">
      <div class="category">
        <div class="column-head">Custom Category</div>
        <div class="column-body">
          <div class="hint">Expenses (Category)</div>
          <div class="line"></div><div class="line"></div><div class="line"></div><div class="line"></div><div class="line"></div>
          <div class="line"></div><div class="line"></div><div class="line"></div><div class="line"></div><div class="line"></div>
        </div>
      </div>
      <div class="plan">
        <div class="column-head">Budget (USD)</div>
        <div class="column-body">
          <div class="hint">What you plan to spend</div>
          <div class="line"></div><div class="line"></div><div class="line"></div><div class="line"></div><div class="line"></div>
          <div class="line"></div><div class="line"></div><div class="line"></div><div class="line"></div><div class="line"></div>
        </div>
      </div>
      <div class="actual">
        <div class="column-head">Actual (USD)</div>
        <div class="column-body">
          <div class="hint">What you actually spent</div>
          <div class="line"></div><div class="line"></div><div class="line"></div><div class="line"></div><div class="line"></div>
          <div class="line"></div><div class="line"></div><div class="line"></div><div class="line"></div><div class="line"></div>
        </div>
      </div>
    </section>

    <section class="formula">
      <div class="formula-bar">
        <span class="term">Net Income</span><span>=</span>
        <span class="term">Gross Income</span><span>-</span>
        <span class="term">Total Expenses</span>
      </div>
      <div class="formula-notes">
        <span>How much money<br>you kept</span><span></span>
        <span>How much money<br>you earned</span><span></span>
        <span>Actual<br>expenses</span>
      </div>
    </section>

    <p class="footer">Visit us at <strong>harlowfinch.com</strong> for personal financial advice!</p>
  </main>
</body>
</html>
```